Website for Pinegrove Tubing Tours

Require a website for a river float in the City of Edmonton. Located on North Saskatchewan River. Will need to be a coded website with incorporated booking system through Fare Harbor software.

Pages include
Home
Pricing
About
FAQ
Contact

Pinegrove Tubing Tours is an activity based business that will have customers floating down the North Saskatchewan river in Edmonton AB. The site will have all information needed and a full reservation system. The project was launched to provide people in the Edmonton area a favorite summer activity.

Here are similar websites to reference what our business will be doing and what we are looking for.

sunnybendpaddles.example
cedarcreekdrifts.example

Target Market(s)

Families, Groups, Individuals, Anyone who wants to explore the river

Industry/Entity Type

Activities based business/ Outdoor recreational/ River Float

Coding

Coded - Design and coding required

Number of Pages Required

5+ page

Colors
0054AA
0677BA
7BADD7
CADEEF
E8F1F8
F0912C
F2A743
F7CA91
FBE8D2
FDF5EE

```html
<!DOCTYPE html>
<html lang="en">
<head>
<meta charset="utf-8">
<title>Pinegrove Tubing Tours</title>
<link href="https://fonts.googleapis.com/css2?family=Baloo+2:wght@700;800&family=Montserrat:wght@400;500;600;700&display=swap" rel="stylesheet">
<style>
:root{
  --blue-deep:#0054AA;
  --blue:#0677BA;
  --blue-mid:#7BADD7;
  --blue-pale:#CADEEF;
  --blue-mist:#E8F1F8;
  --orange-dark:#F0912C;
  --orange:#F2A743;
  --orange-soft:#F7CA91;
  --teal:#183F40;
  --navy:#1D3766;
  --ink:#333;
  --white:#fff;
}
*{box-sizing:border-box;margin:0;padding:0}
html,body{width:1200px;height:3417px;overflow:hidden}
body{position:relative;font-family:'Montserrat',sans-serif;color:var(--ink);background:var(--white)}
.abs{position:absolute}
.display{font-family:'Baloo 2',sans-serif;font-weight:800;font-variant:small-caps;letter-spacing:.5px;line-height:1}
.btn{position:absolute;display:flex;align-items:center;justify-content:center;background:var(--orange);color:var(--white);border-radius:20px;font-size:13px;font-weight:500;text-transform:uppercase;letter-spacing:.3px}

/* hero */
.hero{left:0;top:0;width:1200px;height:680px;background:
  radial-gradient(ellipse 380px 300px at 180px 330px,rgba(60,90,40,.85),transparent 70%),
  radial-gradient(ellipse 360px 380px at 1040px 300px,rgba(150,110,80,.85),transparent 70%),
  linear-gradient(180deg,#3f74b8 0%,#6e9ed6 30%,#8aa9a0 52%,#2f5a58 68%,#1e4646 85%,var(--teal) 100%)}
.logo-badge{left:507px;top:-93px;width:186px;height:196px;border-radius:50%;background:var(--white);display:flex;align-items:flex-end;justify-content:center;padding-bottom:34px}
.logo-name{font-family:'Montserrat',sans-serif;font-weight:700;font-size:13px;color:var(--navy);text-align:center;line-height:1.2;width:120px}
.menu{left:1100px;top:16px;width:34px;text-align:center;color:var(--white);font-size:8px;font-weight:700}
.menu i{display:block;height:2px;background:var(--orange);margin:0 4px 5px}
.hero-title{left:0;top:172px;width:1200px;text-align:center;color:var(--white);font-size:66px}
.hero-text{left:360px;top:316px;width:480px;text-align:center;color:var(--white);font-size:12px;font-weight:600;line-height:1.3}

/* pricing */
.pricing{left:0;top:640px;width:1200px;height:720px;background:var(--teal)}
.pricing .h{left:159px;top:68px;font-size:46px;color:var(--white)}
.pricing .t{color:var(--white);font-size:18px;font-weight:500}
.price{left:159px;top:150px;color:var(--white);font-size:16px;font-weight:500}
.price b{font-family:'Baloo 2',sans-serif;font-size:34px;font-weight:800}
.pricing .p{color:var(--white);font-size:14px;font-weight:500}
.group{left:845px;top:197px;color:var(--white);font-size:18px}
.contact-link{left:845px;top:231px;color:var(--orange);font-size:18px;font-weight:600;border-bottom:1px solid var(--orange);padding-right:4px}
.photo{position:absolute}
.card-title{font-size:18px;font-weight:500;color:var(--white)}
.card-text{font-size:9.5px;color:#dfe7e6;line-height:1.5;width:260px}
.arrow{width:44px;height:44px;border-radius:50%}

/* about */
.about-h{left:159px;top:1412px;font-size:48px;color:var(--blue)}
.about-sub{left:159px;top:1472px;width:420px;font-size:13.5px;font-weight:700;color:#222;line-height:1.3}
.about-p{left:159px;width:420px;font-size:12.2px;line-height:1.45;color:#555}
.about-photo{left:646px;top:1474px;width:386px;height:310px;border-radius:193px 193px 40% 40%;border:7px solid var(--navy);background:linear-gradient(180deg,#6fa0d6 0%,#3f7a3b 35%,#2f6b56 58%,#3d6f8a 78%,#7BADD7 100%)}

/* faq */
.faq{left:0;top:1880px;width:1200px;height:600px;background:linear-gradient(180deg,var(--blue-mist) 0%,#C5DAE7 12%,#C5DAE7 100%)}
.faq-photo{left:0;top:175px;width:520px;height:422px;background:linear-gradient(90deg,rgba(70,120,160,.75) 0%,rgba(100,150,190,.55) 55%,rgba(197,218,231,0) 100%),linear-gradient(180deg,rgba(197,218,231,0) 0%,#9fc0d6 50%,#3d79a6 100%)}
.faq-h{left:160px;top:112px;font-size:48px;color:var(--blue)}
.faq-item{position:absolute;left:579px;width:490px;background:var(--white);box-shadow:0 2px 4px rgba(0,0,0,.06);padding:14px 20px 14px 35px;font-size:11.5px;font-weight:600;color:#333}
.faq-item svg{position:absolute;left:13px;top:16px}
.faq-item p{font-weight:400;font-size:10.5px;line-height:1.7;margin-top:12px;color:#555}

/* contact */
.contact{left:0;top:2477px;width:1200px;height:660px;background:linear-gradient(180deg,var(--white) 0%,#e8dfdc 14%,#cdb7a8 30%,#8c8b7a 42%,#3c5a49 52%,#2b4a3f 70%,#6d857a 86%,var(--white) 100%)}
.contact-h{left:0;top:2770px;width:1200px;text-align:center;color:var(--white);font-size:46px}
.contact-card{left:453px;top:2835px;width:294px;height:258px;background:var(--white);border-radius:4px}
.ci{position:absolute;left:55px;font-size:10.5px;color:#333;line-height:1.4}
.ci svg{position:absolute;left:-21px;top:1px}
.social{width:14px;height:14px;border-radius:50%;background:var(--blue)}

/* footer */
.f-h{font-size:13px;font-weight:700;color:#222;letter-spacing:.4px}
.f-t{font-size:11px;color:#333}
.f-line{left:159px;top:3361px;width:882px;height:1px;background:#ddd}
</style>
</head>
<body>

<section class="abs hero" role="img" aria-label="Photo of a raft floating down a river between forested slopes and steep rocky cliffs"></section>
<div class="abs logo-badge"><span class="logo-name">Pinegrove Tubing Tours</span></div>
<div class="abs menu"><i></i><i></i><i></i>MENU</div>
<h1 class="abs display hero-title">Shuttle Service And<br>Gear Included</h1>
<p class="abs hero-text">We provide everything you need including round trip shuttle service, float tube, lifejacket, paddle, and more. Fun for everyone!</p>
<a class="btn" style="left:537px;top:370px;width:126px;height:36px">Book Now</a>

<section class="abs pricing">
  <h2 class="abs display h">Pricing</h2>
  <p class="abs t" style="left:160px;top:124px">Tube and Shuttle</p>
  <p class="abs price"><b>$30 /</b> person BOOK NOW</p>
  <p class="abs p" style="left:160px;top:206px">We keep our pricing simple and include everything you need:</p>
  <p class="abs p" style="left:160px;top:236px">Premium comfort float tube with backrest and cup holder</p>
  <p class="abs group">Group of 10 or more?</p>
  <a class="abs contact-link">Contact us</a>

  <div class="photo" style="left:131px;top:286px;width:299px;height:234px;background:linear-gradient(180deg,#3e6a34 0%,#5b8d9a 45%,#4f86a0 75%,#3f6e55 100%)" role="img" aria-label="Photo of groups in rafts on a green river"></div>
  <div class="photo" style="left:451px;top:286px;width:298px;height:234px;background:linear-gradient(180deg,#3a3434 0%,#d8532c 30%,#e2603a 65%,#6b3a30 100%)" role="img" aria-label="Photo of orange lifejackets hanging on a rack"></div>
  <div class="photo" style="left:770px;top:286px;width:299px;height:234px;background:linear-gradient(180deg,#c9d1d6 0%,#8d96a0 40%,#b7c3cc 70%,#d65a55 100%)" role="img" aria-label="Photo of paddlers standing on boards in shallow water"></div>

  <svg class="abs arrow" style="left:55px;top:380px" viewBox="0 0 44 44"><circle cx="22" cy="22" r="22" fill="#8d9a9a"/><path d="M30 22H14M20 16l-6 6 6 6" stroke="#fff" stroke-width="2" fill="none"/></svg>
  <svg class="abs arrow" style="left:1100px;top:380px" viewBox="0 0 44 44"><circle cx="22" cy="22" r="22" fill="#8d9a9a"/><path d="M14 22h16M24 16l6 6-6 6" stroke="#fff" stroke-width="2" fill="none"/></svg>

  <p class="abs card-title" style="left:130px;top:540px">Safety training</p>
  <p class="abs card-text" style="left:130px;top:568px">Short briefing on river safety, tube handling and exits before every float.</p>
  <a class="btn" style="left:130px;top:612px;width:126px;height:36px">Book Now</a>

  <p class="abs card-title" style="left:451px;top:540px">Lifejacket</p>
  <p class="abs card-text" style="left:451px;top:568px">Every rider gets a fitted lifejacket, checked by our staff at launch.</p>
  <a class="btn" style="left:451px;top:612px;width:126px;height:36px">Book Now</a>

  <p class="abs card-title" style="left:770px;top:540px">Paddle</p>
  <p class="abs card-text" style="left:770px;top:568px">A light paddle helps you steer around rocks and drift toward shore.</p>
  <a class="btn" style="left:770px;top:612px;width:126px;height:36px">Book Now</a>
</section>

<h2 class="abs display about-h">About Us</h2>
<p class="abs about-sub">Float the North Saskatchewan through downtown Edmonton Edmonton's Best Summer Activity</p>
<p class="abs about-p" style="top:1514px">We provide the lifejacket, paddle, river tube and shuttle service. You just have to show up. Pinegrove Tubing Tours was launched to provide people in the Edmonton area a favorite summer activity. Nothing is better on a hot summer day, than spending it on the river and seeing Edmonton from a new perspective.</p>
<p class="abs about-p" style="top:1610px">Our home base and meeting spot is at Cedar Landing (Map Link), by the Glasshouse Gardens. This is where you will check in, and board the shuttle. The shuttle will take all floaters up river to Willowbank Park Boat Launch, where your tube will be waiting. Once on the river, you can sit back, relax, explore and enjoy the view. Once you complete the float, and arrive back at Cedar Landing, staff will be available to assist in exiting the river where you will return your tube and gear. Safety is our top priority, but having fun is a close second. Don't miss out on Edmonton's best summer activity.</p>
<a class="btn" style="left:159px;top:1787px;width:126px;height:38px;font-size:14px">Book Now</a>
<div class="abs about-photo" role="img" aria-label="Photo of rafters on a calm river lined with trees, with an inflatable tube in front"></div>

<section class="abs faq">
  <div class="abs faq-photo" role="img" aria-label="Photo of two stand-up paddleboarders on open water"></div>
  <h2 class="abs display faq-h">FAQ</h2>
</section>
<div class="faq-item" style="top:1996px;height:110px"><svg width="11" height="11" viewBox="0 0 11 11"><circle cx="5.5" cy="5.5" r="5.5" fill="var(--blue)"/><text x="5.5" y="8.5" font-size="8" fill="#fff" text-anchor="middle" font-family="Montserrat,sans-serif" font-weight="700">?</text></svg>How do I reserve my float?<p>We highly recommend booking online, as we do sell out. BOOK NOW Floats can also be reserved on-site at Cedar Landing, on a first come first serve basis.</p></div>
<div class="faq-item" style="top:2120px;height:43px"><svg width="11" height="11" viewBox="0 0 11 11"><circle cx="5.5" cy="5.5" r="5.5" fill="var(--blue)"/><text x="5.5" y="8.5" font-size="8" fill="#fff" text-anchor="middle" font-family="Montserrat,sans-serif" font-weight="700">?</text></svg>What safety information should I know?</div>
<div class="faq-item" style="top:2179px;height:43px"><svg width="11" height="11" viewBox="0 0 11 11"><circle cx="5.5" cy="5.5" r="5.5" fill="var(--blue)"/><text x="5.5" y="8.5" font-size="8" fill="#fff" text-anchor="middle" font-family="Montserrat,sans-serif" font-weight="700">?</text></svg>What is included?</div>
<div class="faq-item" style="top:2234px;height:43px"><svg width="11" height="11" viewBox="0 0 11 11"><circle cx="5.5" cy="5.5" r="5.5" fill="var(--blue)"/><text x="5.5" y="8.5" font-size="8" fill="#fff" text-anchor="middle" font-family="Montserrat,sans-serif" font-weight="700">?</text></svg>What should I bring?</div>
<div class="faq-item" style="top:2290px;height:43px"><svg width="11" height="11" viewBox="0 0 11 11"><circle cx="5.5" cy="5.5" r="5.5" fill="var(--blue)"/><text x="5.5" y="8.5" font-size="8" fill="#fff" text-anchor="middle" font-family="Montserrat,sans-serif" font-weight="700">?</text></svg>Where are you located?</div>
<a class="btn" style="left:578px;top:2368px;width:125px;height:36px">View All</a>

<section class="abs contact" role="img" aria-label="Photo of a city skyline above a river valley with a bridge and trees"></section>
<h2 class="abs display contact-h">We'd Love To Hear From You!</h2>
<div class="abs contact-card">
  <p class="ci" style="top:30px"><svg width="10" height="13" viewBox="0 0 10 13"><path d="M5 0a5 5 0 0 0-5 5c0 4 5 8 5 8s5-4 5-8a5 5 0 0 0-5-5z" fill="var(--blue)"/><circle cx="5" cy="5" r="2" fill="#fff"/></svg>Cedar Landing 4120 Riverside Ave<br>NW, Edmonton, AB</p>
  <p class="ci" style="top:74px"><svg width="12" height="12" viewBox="0 0 12 12"><path d="M2 0l3 3-1.5 2a7 7 0 0 0 3.5 3.5L9 7l3 3-2 2C5 12 0 7 0 2z" fill="var(--blue)"/></svg>780 555 0142</p>
  <p class="ci" style="top:102px"><svg width="12" height="9" viewBox="0 0 12 9"><rect width="12" height="9" rx="1" fill="var(--blue)"/><path d="M0 1l6 4 6-4" stroke="#fff" fill="none"/></svg>info@pinegrovetubing.example</p>
  <div class="abs social" style="left:100px;top:147px" aria-label="Social link"></div>
  <div class="abs social" style="left:133px;top:147px" aria-label="Social link"></div>
  <div class="abs social" style="left:166px;top:147px" aria-label="Social link"></div>
  <a class="btn" style="left:84px;top:193px;width:126px;height:36px">Contact Us</a>
</div>

<footer>
  <p class="abs f-h" style="left:265px;top:3158px">PINEGROVE TUBING TOURS</p>
  <p class="abs f-h" style="left:266px;top:3188px;font-size:12px">CONNECT</p>
  <p class="abs f-t" style="left:288px;top:3221px"><svg class="abs" style="left:-21px;top:2px" width="12" height="9" viewBox="0 0 12 9"><rect width="12" height="9" rx="1" fill="#333"/><path d="M0 1l6 4 6-4" stroke="#fff" fill="none"/></svg>info@pinegrovetubing.example</p>
  <p class="abs f-t" style="left:288px;top:3254px;line-height:1.3"><svg class="abs" style="left:-21px;top:2px" width="10" height="13" viewBox="0 0 10 13"><path d="M5 0a5 5 0 0 0-5 5c0 4 5 8 5 8s5-4 5-8a5 5 0 0 0-5-5z" fill="#333"/><circle cx="5" cy="5" r="2" fill="#fff"/></svg>Cedar Landing 4120 Riverside Ave<br>NW, Edmonton, AB</p>
  <div class="abs social" style="left:267px;top:3307px;background:#333" aria-label="Social link"></div>
  <div class="abs social" style="left:301px;top:3307px;background:#333" aria-label="Social link"></div>
  <div class="abs social" style="left:337px;top:3307px;background:#333" aria-label="Social link"></div>

  <p class="abs f-h" style="left:552px;top:3158px">FLOATING 7 DAYS A WEEK</p>
  <p class="abs" style="left:590px;top:3220px;width:115px;text-align:center;font-size:12px;font-weight:700;color:#555;line-height:1.25">Pinegrove Tubing Tours</p>
  <div class="abs" style="left:491px;top:3308px;width:203px;height:36px;border:1px solid #ccc;font-size:10px;color:#777;padding:12px 12px">Enter Your Email</div>
  <div class="abs" style="left:694px;top:3308px;width:124px;height:36px;background:var(--orange);color:#fff;font-size:9.5px;font-weight:600;display:flex;align-items:center;justify-content:center">SUBSCRIBE NOW</div>

  <p class="abs f-h" style="left:853px;top:3188px;font-size:12px">NAVIGATION</p>
  <p class="abs f-t" style="left:853px;top:3220px">About</p>
  <p class="abs f-t" style="left:853px;top:3247px">Pricing</p>
  <p class="abs f-t" style="left:853px;top:3273px">FAQ</p>
  <p class="abs f-t" style="left:853px;top:3300px">Contact</p>

  <div class="abs f-line"></div>
  <p class="abs f-t" style="left:0;top:3382px;width:1200px;text-align:center;color:#666">©2022 Pinegrove Tubing Tours.</p>
</footer>

</body>
</html>
```